【サイトマップ】
1 TOP
2 rema sol +とは
3 お客様の声(一覧)
4 お客様の声(詳細)
5 ブログ(一覧)
6 ブログ(詳細)
7 お知らせ(一覧)
8 お知らせ(詳細)
9 イベント情報(一覧)
10 イベント情報(詳細)
11 お問い合わせ
12 Q&A
13 商品ページ(一覧)
14 商品ページ(詳細)
15 ライター紹介ページ

【要望】
情報発信サイトのため静的なページは最低限押さえ動的なコンテンツを盛り込んでおります。
各ページの意図を説明しておきます。

<ブログ>
いわゆるコラムページです。季節に合わせた着こなしやおすすめのコーディネートなどを紹介していきます。

<お客様の声>
商品レビュー。ECで購入した商品についてお客様の感想を掲載します。

<イベント情報>
着こなし講座。お食事会などイベントについて掲載していきます。

<商品ページ>
ライターが連動しているECサイトから商品をピックアップし記事として取り上げます。

<ライター紹介ページ>
まずはライターは2名体勢で指導しますが今後増やしていく予定です。
TOPに2名分の枠を用意頂ければと思います。
参考:https://norbeta.co.jp/member

■HPのメインターゲット
30、40代の方(女性のみ)

■サイトのデザインにおける優先事項
見やすさ > デザイン性(写真・画像量)

■HPに望む効果
・新規顧客獲得
ECサイトも立ち上げ前なので、とにかくサイトのファンを付けたいと考えております。
そのため「人目につくサイト」「定期的にチェックしてみたいと思ってもらえるサイト」を目指しております。
ページ数
1ページ
希望イメージ
シンプル 複雑
単色 カラフル
暗い 明るい
日常 高級
遊び心 厳粛
未来的 伝統的
女性的 男性的
希望する色
特にございません。いろんな提案を見てみたいのが正直なところです。
納品ファイル
• イラストレーター形式 (.ai)
• フォトショップ形式 (.psd)
• PNG形式 (.png)
補足説明
<店舗へのご連絡はおやめください>
ジョブリオの規約にもありますが、店舗様の通常業務に支障が出るため・素材について直接電話等のお問い合わせをお控えいただきますよう、ご協力の程お願いいたします。

-----------------------------------------------------------------------

<素材はPixmoraかその他無償の素材をご使用ください>
素材として必要なものがある場合にはピクモラ画像をご使用ください。
疑問や不明点などがありましたら、ジョブリオ内メッセージにて頂戴できますと幸いです。

その際、定期契約でダウンロード出来る画像のみを使用してください。
(画像検索した際に出てくるサムネール下の画像番号の横に
ピクモラのマークがあるものは使用しないようお願いいたします。)

ピクモラ以外の素材を使用する際には、
必ず無料で提供いただける物のみご使用ください。
もう少し提案を見たいため延長させて頂きます。
もう少し提案が見たいため、延長させて頂きます。
本日より1週間募集期間を延長致します。
引き続き宜しくお願い致します。
沢山のご提案をありがとうございます。
最後にあと一週間だけ期間を延長させていただきます。
引き続き、何卒宜しくお願い致します。

ひと目見て気に入りました。

みなさまご提案ありがとうございました。

```html
<!DOCTYPE html>
<html lang="ja">
<head>
<meta charset="utf-8">
<title>rema sol + | 30代・40代女性のためのファッション情報</title>
<link rel="stylesheet" href="https://fonts.googleapis.com/css2?family=Quicksand:wght@500;700&family=Noto+Sans+JP:wght@400;500;700&display=swap">
<style>
:root{
  --cream:#fdf3ea;
  --cream-deep:#f8e6d6;
  --orange:#e0873a;
  --orange-deep:#d77a2e;
  --orange-soft:#eba262;
  --ink:#3a2e27;
  --muted:#8a7b71;
  --line:#ead6c4;
  --white:#ffffff;
  --photo-warm:#c9b3a0;
  --photo-dark:#7d6b5e;
  --photo-green:#6f7b5c;
}
*{box-sizing:border-box;margin:0;padding:0}
html,body{width:1200px;height:2912px;overflow:hidden}
body{background:var(--cream);color:var(--ink);font-family:"Noto Sans JP",sans-serif;font-size:13px;line-height:1.6;position:relative}
.en{font-family:"Quicksand",sans-serif}

/* header */
.site-header{height:184px;position:relative}
.logo{position:absolute;left:0;right:0;top:30px;text-align:center;font-family:"Quicksand",sans-serif;font-weight:700;font-size:46px;color:var(--orange);letter-spacing:2px}
.header-icons{position:absolute;right:92px;top:100px;display:flex;gap:18px}
.header-icons svg{width:20px;height:20px;fill:var(--orange)}
.global-nav{position:absolute;left:0;right:0;top:136px;height:36px;border-top:1px solid var(--line);border-bottom:1px solid var(--line);background:var(--white);display:flex;justify-content:center;align-items:center;gap:58px;font-size:11px;color:var(--muted)}

/* hero */
.hero{position:absolute;top:200px;left:88px;width:1024px;height:392px;display:flex}
.hero-visual{width:784px;height:392px;background:linear-gradient(110deg,#d9c9b9,#a89485 45%,#6e5f55);position:relative}
.hero-caption{position:absolute;left:28px;top:228px;display:flex;flex-direction:column;gap:12px}
.hero-caption span{align-self:flex-start;background:var(--ink);color:var(--white);font-weight:700;font-size:19px;padding:6px 14px}
.ranking{width:240px;height:392px;background:var(--white);padding:26px 16px}
.ranking h2{font-family:"Quicksand",sans-serif;font-weight:700;color:var(--orange);font-size:26px;text-align:center;line-height:1;margin-bottom:18px}
.rank-item{display:flex;gap:10px;margin-bottom:22px;position:relative}
.rank-thumb{width:56px;height:56px;flex:none;background:var(--photo-warm)}
.rank-no{position:absolute;left:-6px;top:-6px;width:20px;height:20px;border-radius:50%;background:var(--orange);color:var(--white);font-size:11px;font-weight:700;text-align:center;line-height:20px}
.rank-text{font-size:10px;line-height:1.6;color:var(--ink)}

/* section heads */
.section-head{text-align:center}
.section-head h2{font-family:"Quicksand",sans-serif;font-weight:700;color:var(--orange);font-size:28px;line-height:1}
.section-head p{font-size:10px;color:var(--orange);margin-top:4px}

/* articles */
.new-article{position:absolute;top:640px;left:88px;width:1024px}
.card-row{display:flex;gap:21px;margin-top:24px}
.card{width:240px}
.card-photo{height:240px;background:linear-gradient(160deg,#e8ded5,#b9a291 55%,#6a564a)}
.card h3{font-size:15px;font-weight:700;margin-top:18px}
.card p{font-size:10px;color:var(--ink);margin-top:4px;line-height:1.7}

/* products */
.products{position:absolute;top:1100px;left:88px;width:1024px}
.product-photo{height:240px;background:linear-gradient(170deg,#9ba486,#6f7b5c 50%,#4b5040)}
.product h3{font-size:14px;font-weight:700;margin-top:16px}
.product .price{font-size:10px;margin-top:2px}
.product .more{display:block;margin-top:14px;height:28px;border:1px solid var(--line);background:var(--white);text-align:center;line-height:26px;font-size:10px;color:var(--muted)}

/* about */
.about{position:absolute;top:1592px;left:0;width:1200px;height:848px;background:radial-gradient(circle at 20% 25%,var(--orange-soft),transparent 30%),radial-gradient(circle at 85% 70%,var(--orange-soft),transparent 28%),var(--orange);text-align:center;color:var(--ink)}
.about .section-head{margin-top:90px}
.about .section-head h2{color:var(--ink);font-size:30px}
.about .section-head h2 b{color:var(--white);font-weight:700}
.about .section-head p{color:var(--ink)}
.about-lead{margin-top:36px;font-weight:700;font-size:22px;line-height:1.6}
.about-body{margin-top:30px;font-size:11px;line-height:2;color:var(--ink)}
.about-body p+p{margin-top:14px}
.writer .section-head{margin-top:44px}
.writer .section-head h2{color:var(--white);font-size:26px}
.writer .section-head p{color:var(--white)}
.writer-box{margin:10px auto 0;width:440px;height:228px;background:var(--white);border-radius:26px;display:flex;justify-content:center;gap:90px;padding-top:28px}
.writer-card{text-align:center}
.writer-photo{width:140px;height:140px;border-radius:50%;background:linear-gradient(180deg,#d8cbc0,#8f7e72)}
.writer-card p{margin-top:10px;font-size:12px}

/* info */
.info{position:absolute;top:2520px;left:88px;width:1024px;display:flex;gap:16px}
.info-box{flex:1;background:var(--white);padding:20px 24px 22px}
.info-box h2{font-family:"Quicksand",sans-serif;font-weight:700;color:var(--orange);font-size:24px;line-height:1}
.info-box h2 small{font-family:"Noto Sans JP",sans-serif;font-size:9px;font-weight:400;margin-left:6px}
.info-box ul{list-style:none;margin-top:12px;border-top:1px solid var(--line)}
.info-box li{display:flex;gap:24px;font-size:11px;padding:7px 0;border-bottom:1px dotted var(--line)}
.info-box time{color:var(--orange);font-weight:500}

/* footer */
.site-footer{position:absolute;top:2780px;left:0;width:1200px;height:132px;text-align:center}
.footer-nav{display:flex;justify-content:center;gap:30px;font-size:10px;color:var(--muted);padding:14px 0;border-top:1px solid var(--line);border-bottom:1px solid var(--line);margin:0 88px}
.copyright{font-size:10px;color:var(--muted);margin-top:22px}
</style>
</head>
<body>

<header class="site-header">
  <div class="logo">rema sol +</div>
  <div class="header-icons">
    <svg viewBox="0 0 20 20" aria-label="マイページ"><circle cx="10" cy="6" r="4.5"/><path d="M1 19c0-5 4-8 9-8s9 3 9 8z"/></svg>
    <svg viewBox="0 0 20 20" aria-label="お気に入り"><path d="M10 18 2.5 10.5A4.5 4.5 0 0 1 10 4a4.5 4.5 0 0 1 7.5 6.5z"/></svg>
    <svg viewBox="0 0 20 20" aria-label="カート"><path d="M1 2h3l2.5 10h10L19 5H6" fill="none" stroke="#e0873a" stroke-width="2"/><circle cx="8" cy="16.5" r="1.8"/><circle cx="15" cy="16.5" r="1.8"/></svg>
    <svg viewBox="0 0 20 20" aria-label="検索"><circle cx="8" cy="8" r="5.5" fill="none" stroke="#e0873a" stroke-width="2.4"/><path d="m12 12 6 6" stroke="#e0873a" stroke-width="2.6"/></svg>
  </div>
  <nav class="global-nav en">
    <span>top</span><span>what is rema sol + ?</span><span>blog</span><span>products</span><span>events</span><span>contact</span><span>Q&amp;A</span>
  </nav>
</header>

<section class="hero">
  <div class="hero-visual" role="img" aria-label="椅子に座るリラックスした装いの女性の写真">
    <div class="hero-caption">
      <span>オフスタイルの定番</span>
      <span>リラックスコーデブランド5選</span>
    </div>
  </div>
  <aside class="ranking">
    <h2>ranking</h2>
    <div class="rank-item"><span class="rank-no">1</span><div class="rank-thumb" role="img" aria-label="記事サムネイル写真"></div><p class="rank-text">秋のおでかけに使える<br>きれいめカジュアルの<br>着こなしポイント</p></div>
    <div class="rank-item"><span class="rank-no">2</span><div class="rank-thumb" role="img" aria-label="記事サムネイル写真"></div><p class="rank-text">大人のためのニット<br>選びで失敗しない<br>三つのコツを紹介</p></div>
    <div class="rank-item"><span class="rank-no">3</span><div class="rank-thumb" role="img" aria-label="記事サムネイル写真"></div><p class="rank-text">週末のランチ会に<br>ちょうどいいワンピ<br>コーデをご提案</p></div>
    <div class="rank-item"><span class="rank-no">4</span><div class="rank-thumb" role="img" aria-label="記事サムネイル写真"></div><p class="rank-text">小物で差がつく<br>季節の変わり目の<br>重ね着テクニック</p></div>
  </aside>
</section>

<section class="new-article">
  <div class="section-head"><h2>new article</h2><p>新着記事</p></div>
  <div class="card-row">
    <article class="card"><div class="card-photo" role="img" aria-label="コーディネート記事の写真"></div><h3>タイトル</h3><p>季節に合わせた大人の着こなしを<br>わかりやすくご紹介しています。</p></article>
    <article class="card"><div class="card-photo" role="img" aria-label="コーディネート記事の写真"></div><h3>タイトル</h3><p>季節に合わせた大人の着こなしを<br>わかりやすくご紹介しています。</p></article>
    <article class="card"><div class="card-photo" role="img" aria-label="コーディネート記事の写真"></div><h3>タイトル</h3><p>季節に合わせた大人の着こなしを<br>わかりやすくご紹介しています。</p></article>
    <article class="card"><div class="card-photo" role="img" aria-label="コーディネート記事の写真"></div><h3>タイトル</h3><p>季節に合わせた大人の着こなしを<br>わかりやすくご紹介しています。</p></article>
  </div>
</section>

<section class="products">
  <div class="section-head"><h2>products</h2><p>商品一覧</p></div>
  <div class="card-row">
    <article class="card product"><div class="product-photo" role="img" aria-label="植物の前に立つ女性の商品着用写真"></div><h3>商品名</h3><p class="price">&yen;0,000（税込）</p><span class="more">MORE</span></article>
    <article class="card product"><div class="product-photo" role="img" aria-label="植物の前に立つ女性の商品着用写真"></div><h3>商品名</h3><p class="price">&yen;0,000（税込）</p><span class="more">MORE</span></article>
    <article class="card product"><div class="product-photo" role="img" aria-label="植物の前に立つ女性の商品着用写真"></div><h3>商品名</h3><p class="price">&yen;0,000（税込）</p><span class="more">MORE</span></article>
    <article class="card product"><div class="product-photo" role="img" aria-label="植物の前に立つ女性の商品着用写真"></div><h3>商品名</h3><p class="price">&yen;0,000（税込）</p><span class="more">MORE</span></article>
  </div>
</section>

<section class="about">
  <div class="section-head"><h2>what is <b>rema sol +</b> ?</h2><p>rema sol + とは</p></div>
  <p class="about-lead">いち早く最新のトレンドを押さえたい<br>おしゃれに敏感なあなたのために</p>
  <div class="about-body">
    <p>毎日の服選び、もっと楽しくしませんか。忙しい30代・40代の女性に向けて、<br>季節ごとの着こなしやおすすめのコーディネートを、わかりやすくお届けします。</p>
    <p>ライターが実際に選んだアイテムや、お客様の声、着こなし講座などのイベント情報まで。<br>読むたびに新しい発見があるように、定期的に更新していきます。</p>
    <p>自分らしいおしゃれを見つけるお手伝いを。気になる記事からぜひご覧ください。</p>
    <p>明日の私がもっと好きになる、そんなきっかけをここから。<br>あなたのお気に入りの一着が見つかりますように。</p>
  </div>
  <div class="writer">
    <div class="section-head"><h2>writer</h2><p>ライター紹介</p></div>
    <div class="writer-box">
      <div class="writer-card"><div class="writer-photo" role="img" aria-label="ライターのプロフィール写真"></div><p>ライター</p></div>
      <div class="writer-card"><div class="writer-photo" role="img" aria-label="ライターのプロフィール写真"></div><p>ライター</p></div>
    </div>
  </div>
</section>

<section class="info">
  <div class="info-box">
    <h2>events<small>イベント</small></h2>
    <ul>
      <li><time>2016.00.00</time><span>タイトルタイトルタイトルタイトルタイトル</span></li>
      <li><time>2016.00.00</time><span>タイトルタイトルタイトルタイトルタイトル</span></li>
      <li><time>2016.00.00</time><span>タイトルタイトルタイトルタイトルタイトル</span></li>
      <li><time>2016.00.00</time><span>タイトルタイトルタイトルタイトルタイトル</span></li>
    </ul>
  </div>
  <div class="info-box">
    <h2>news<small>お知らせ</small></h2>
    <ul>
      <li><time>2016.00.00</time><span>タイトルタイトルタイトルタイトルタイトル</span></li>
      <li><time>2016.00.00</time><span>タイトルタイトルタイトルタイトルタイトル</span></li>
      <li><time>2016.00.00</time><span>タイトルタイトルタイトルタイトルタイトル</span></li>
      <li><time>2016.00.00</time><span>タイトルタイトルタイトルタイトルタイトル</span></li>
    </ul>
  </div>
</section>

<footer class="site-footer">
  <nav class="footer-nav">
    <span>TOP</span><span>rema sol +とは</span><span>ブログ</span><span>商品一覧</span><span>イベント</span><span>お知らせ</span><span>お客様の声</span><span>ライター紹介</span><span>お問い合わせ</span><span>Q&amp;A</span>
  </nav>
  <p class="copyright">Copyright &copy;2016 rema sol +. All Rights Reserved.</p>
</footer>

</body>
</html>
```